Fern Assembly Business Cards

Looking or a business card design for my start-up, called "Fern Assembly".
Our tagline is "Unleashing the human potential for good through leadership, culture, and education."
Our mission-driven work includes professional/personal development workshops, educational design services, organizational & project management consulting, and coaching services for K-12 schools, organizations, and individuals.
You can check out the website we're building at fernassembly.example
I select projects from designers who are highly responsive to feedback, engage in dialog about revisions, and provide all root/source documents (so please state in your initial submission that you agree to do so).
Looking forward to seeing your great designs!!
Updates
Hello everyone,
Industry/Entity Type
Building
Requirements
Must have
- Looking for a two sided design that includes our logo (I am uploading two variations that I would like incorporated in .ai format) and website on both sides.
The front side must include:
Logo, Name, Title, Phone, Email, Twitter handle
The back side must include: Logo, @fernassem (our organizational twitter handle)
Nice to have
- I like the rounded corner business cards, but that is not absolutely essential.
Should not have
- Colors beyond those presented in our logo.

```html
<!DOCTYPE html>
<html lang="en">
<head>
<meta charset="utf-8">
<title>Fern Assembly Business Cards</title>
<link rel="stylesheet" href="https://fonts.googleapis.com/css2?family=Cinzel:wght@400&family=Lato:wght@400;700&display=swap">
<style>
  :root {
    --page-bg: #e6e9ea;
    --card-white: #ffffff;
    --card-dark: #2e2e2e;
    --sky: #8ecfe6;
    --sky-pale: #e6f4fa;
    --stone: #a8a198;
    --stone-light: #cfc9c2;
    --ink: #1f1f1f;
    --icon-blue: #7fbfdc;
  }
  * { box-sizing: border-box; margin: 0; padding: 0; }
  html, body { width: 1200px; height: 960px; overflow: hidden; }
  body {
    background: var(--page-bg);
    position: relative;
    font-family: "Lato", Arial, sans-serif;
  }
  .card {
    position: absolute;
    left: 250px;
    width: 700px;
    height: 400px;
    border-radius: 34px;
    overflow: hidden;
    box-shadow: 0 10px 30px rgba(0,0,0,0.18);
  }

  /* Front */
  .card--front { top: 40px; background: var(--card-white); }
  .front__decor { position: absolute; left: 0; top: 0; width: 700px; height: 400px; }
  .front__brand {
    position: absolute; left: 330px; top: 52px; width: 330px; text-align: center;
  }
  .brand-mark {
    display: block; width: 64px; height: 64px; border-radius: 50%;
    background: var(--sky); margin: 0 auto 14px;
  }
  .brand-name {
    font-family: "Cinzel", Georgia, serif; font-weight: 400;
    color: var(--stone); font-size: 30px; letter-spacing: 1px; line-height: 1;
  }
  .brand-pillars {
    font-family: "Cinzel", Georgia, serif; color: var(--stone);
    font-size: 9.5px; letter-spacing: 3.4px; margin-top: 6px;
  }
  .brand-site {
    font-family: "Cinzel", Georgia, serif; text-transform: lowercase;
    color: var(--stone); font-size: 11px; margin-top: 6px; letter-spacing: 0.5px;
  }
  .front__person {
    position: absolute; left: 330px; top: 222px; color: var(--ink);
  }
  .person-name { font-size: 24px; font-weight: 400; }
  .person-title { font-size: 14px; text-transform: uppercase; margin-left: 4px; }
  .contact-list { list-style: none; margin-top: 16px; }
  .contact-list li {
    display: flex; align-items: center; gap: 12px;
    font-size: 15px; margin-bottom: 12px;
  }
  .contact-icon { width: 18px; height: 18px; flex: none; }

  /* Back */
  .card--back { top: 500px; background: var(--card-dark); text-align: center; }
  .back__brand { position: absolute; left: 0; right: 0; top: 58px; }
  .back__brand .brand-mark { width: 110px; height: 110px; margin-bottom: 28px; }
  .back__brand .brand-name { font-size: 46px; color: var(--stone-light); letter-spacing: 2px; }
  .back-tagline {
    font-family: "Cinzel", Georgia, serif; color: var(--stone-light);
    font-size: 12.5px; letter-spacing: 2.6px; line-height: 1.35; margin-top: 8px;
  }
  .back-site {
    font-family: "Cinzel", Georgia, serif; text-transform: lowercase;
    color: var(--stone-light); font-size: 13px; margin-top: 10px; letter-spacing: 0.5px;
  }
  .back-handle {
    display: inline-flex; align-items: center; gap: 8px;
    color: var(--stone-light); font-size: 14px; margin-top: 10px;
  }
  .handle-square { width: 11px; height: 11px; background: var(--stone-light); border-radius: 2px; }
</style>
</head>
<body>

  <section class="card card--front" aria-label="Business card front">
    <svg class="front__decor" viewBox="0 0 700 400" aria-hidden="true">
      <path d="M0 0 H190 C290 60 320 200 320 400 H0 Z" fill="var(--sky-pale)"/>
    </svg>

    <div class="front__brand">
      <span class="brand-mark"></span>
      <div class="brand-name">FERN ASSEMBLY</div>
      <div class="brand-pillars">LEADERSHIP | CULTURE | EDUCATION</div>
      <div class="brand-site">www.fernassembly.example</div>
    </div>

    <div class="front__person">
      <p><span class="person-name">Dana Whitlock</span><span class="person-title">| Director</span></p>
      <ul class="contact-list">
        <li>
          <svg class="contact-icon" viewBox="0 0 18 18" aria-hidden="true">
            <rect x="4" y="1" width="10" height="16" rx="2" fill="none" stroke="var(--icon-blue)" stroke-width="1.6"/>
            <line x1="7" y1="14" x2="11" y2="14" stroke="var(--icon-blue)" stroke-width="1.6"/>
          </svg>
          208-555-0147
        </li>
        <li>
          <svg class="contact-icon" viewBox="0 0 18 18" aria-hidden="true">
            <rect x="1" y="4" width="16" height="11" fill="none" stroke="var(--icon-blue)" stroke-width="1.6"/>
            <polyline points="1,4 9,11 17,4" fill="none" stroke="var(--icon-blue)" stroke-width="1.6"/>
          </svg>
          dana@fernassembly.example
        </li>
        <li>
          <svg class="contact-icon" viewBox="0 0 18 18" aria-hidden="true">
            <rect x="2" y="2" width="14" height="14" rx="2" fill="var(--icon-blue)"/>
          </svg>
          @whitlockdana
        </li>
      </ul>
    </div>
  </section>

  <section class="card card--back" aria-label="Business card back">
    <div class="back__brand">
      <span class="brand-mark"></span>
      <div class="brand-name">FERN ASSEMBLY</div>
      <div class="back-tagline">UNLEASHING THE HUMAN POTENTIAL FOR GOOD THROUGH<br>LEADERSHIP, CULTURE, AND EDUCATION</div>
      <div class="back-site">www.fernassembly.example</div>
      <div class="back-handle"><span class="handle-square"></span>@fernassem</div>
    </div>
  </section>

</body>
</html>
```